Entrepreneur needs a business card design

I need a business card to name my three companies, as well as contact information.
I'm open on design and color and it can be plain or complex. I'm open on colors but I think I prefer something somewhat formal but fun as well.
I'm open on whether the background is plain or has design in it. I don't have company logos.
Target Market(s)
Auto dealers, realtors and property managers
Industry/Entity Type
Business
Contact Information for Business Card
HALVERSEN FAMILY PROPERTIES, LLC
HALVERSEN PUBLISHING, LLC
MOTORVANE CONSULTING, LLC
Lee Halversen
2871 W. Tamarind Ave. #419
Boise, Idaho 83719-2056
208-514-3092
lee@halv3rn.com

```html
<!DOCTYPE html>
<html lang="en">
<head>
<meta charset="utf-8">
<title>Halversen Business Card</title>
<link rel="stylesheet" href="https://fonts.googleapis.com/css2?family=Josefin+Sans:wght@300&display=swap">
<style>
  :root {
    --page-bg: #eeeff1;
    --card-bg: #fbfbfb;
    --ink: #3a3a3a;
    --stripe-teal: #0f6a6b;
    --stripe-mustard: #d9a514;
    --stripe-rust: #c95a35;
    --stripe-sand: #cfc9a2;
    --stripe-blue: #3a5595;
  }
  html, body {
    margin: 0;
    width: 1200px;
    height: 1200px;
    overflow: hidden;
    background: var(--page-bg);
  }
  .card {
    position: absolute;
    left: 100px;
    top: 314px;
    width: 1000px;
    height: 572px;
    background: var(--card-bg);
    box-shadow: 0 6px 24px rgba(0, 0, 0, 0.12);
    font-family: "Josefin Sans", sans-serif;
    font-weight: 300;
    color: var(--ink);
  }
  .stripe-bar {
    display: flex;
    height: 12px;
  }
  .stripe-bar span { flex: 1; }
  .stripe-teal { background: var(--stripe-teal); }
  .stripe-mustard { background: var(--stripe-mustard); }
  .stripe-rust { background: var(--stripe-rust); }
  .stripe-sand { background: var(--stripe-sand); }
  .stripe-blue { background: var(--stripe-blue); }
  .companies {
    position: absolute;
    left: 70px;
    top: 150px;
    width: 430px;
    margin: 0;
    padding: 0;
    list-style: none;
    text-align: center;
    text-transform: uppercase;
    font-size: 31px;
    line-height: 1.35;
    letter-spacing: 0.02em;
  }
  .companies li + li { margin-top: 34px; }
  .contact {
    position: absolute;
    right: 70px;
    top: 56px;
    margin: 0;
    text-align: right;
    font-style: normal;
    font-size: 27px;
    line-height: 1.5;
  }
</style>
</head>
<body>
  <section class="card">
    <div class="stripe-bar">
      <span class="stripe-teal"></span>
      <span class="stripe-mustard"></span>
      <span class="stripe-rust"></span>
      <span class="stripe-sand"></span>
      <span class="stripe-blue"></span>
    </div>
    <ul class="companies">
      <li>Halversen Family<br>Properties, LLC</li>
      <li>Halversen<br>Publishing, LLC</li>
      <li>Motorvane<br>Consulting, LLC</li>
    </ul>
    <address class="contact">
      Lee Halversen<br>
      2871 W. Tamarind Ave.<br>
      #419 Boise,<br>
      Idaho 83719-2056<br>
      208-514-3092<br>
      lee@halv3rn.com
    </address>
  </section>
</body>
</html>
```